SIGN UP PAGE AND CHECK OUT PROCESS DESIGN NEEDED

I offer a subscription service. Two products that offer the same exact features just two different prices as the cheaper product offers limited of all the features....<br/><br/>PLEASE USE EXISTING THEME OF CURRENT DESIGN JUST MAKE AN IMPROVED SIGN UP PAGE. <br/><br/><br/>NEED SIGN UP PAGE for a subscription service..... <br/>This is my current sign up page, only offers one product: https://www.brightloomrewards.biz/?page=signup <br/><br/>Please use all the same fields and content listed on this sign up page also please do a fake sign up to see the credit card page. I also need the credit card page to be designed....or if you want to combine the sign up and credit card page, etc. all in one I am open for that too....my goal is a super quick an easy sign up for customer. <br/><br/> AL A CARTE PROGRAM<br/>1 CERTIFICATE TYPE EACH MONTH<br/>$49/MTH MONTH TO MONTH BASIS NO CONTRACTS<br/>$239 ONE TIME PAYMENT FOR 6 MTHS OF SERVICE<br/>$399 ONE TIME PAYMENT FOR 12 MONTHS OF SERVICE<br/><br/>FEATURES:<br/><br/>UNLIMITED CERTIFICATE PDF DOWNLOADS<br/><br/>UNLIMITED E-MAIL CERTIFICATES<br/><br/>UNLIMITED TEXT/SMS CERTIFICATES<br/><br/>UNLIMITED API USAGE<br/><br/>UNLIMITED WEB BANNER CERTIFICATES<br/><br/>FULL REDEMPTION TRACKING<br/><br/>CERTIFICATE DISTRIBUTION REPORTS<br/><br/>WHITE LABEL REDEMPTION SITE<br/><br/>END USER MARKETING VIDEOS<br/><br/>MARKETING POSTERS AND FLYERS<br/><br/>PRODUCT DESCRIPTIONI BROCHURES<br/><br/>THE LATEST TIPS<br/><br/>SEPERATE REDEMPTION WEBSITES<br/><br/>CONTACT US 24/7<br/><br/>AFFILIATE PROGRAM<br/><br/>DISCOUNT TRAVEL BOOKING ENGINE<br/><br/>UNLIMITED PROGRAM<br/>UNLIMITED AMOUNTS OF ALL THE CERTIFICATES<br/>$99/MTH MONTH TO MONTH BASIS NO CONTRACTS<br/>$495 ONE TIME PAYMENT FOR 6 MTHS OF SERVICE<br/>$2,295 ONE TIME PAYMENT FOR 12 MONTHS OF SERVICE<br/><br/>FEATURES:<br/><br/>UNLIMITED CERTIFICATE PDF DOWNLOADS<br/><br/>UNLIMITED E-MAIL CERTIFICATES<br/><br/>UNLIMITED TEXT/SMS CERTIFICATES<br/><br/>UNLIMITED API USAGE<br/><br/>UNLIMITED WEB BANNER CERTIFICATES<br/><br/>FULL REDEMPTION TRACKING<br/><br/>CERTIFICATE DISTRIBUTION REPORTS<br/><br/>WHITE LABEL REDEMPTION SITE<br/><br/>END USER MARKETING VIDEOS<br/><br/>MARKETING POSTERS AND FLYERS<br/><br/>PRODUCT DESCRIPTIONI BROCHURES<br/><br/>THE LATEST TIPS<br/><br/>SEPERATE REDEMPTION WEBSITES<br/><br/>CONTACT US 24/7<br/><br/>AFFILIATE PROGRAM<br/><br/>DISCOUNT TRAVEL BOOKING ENGINE<br/><br/><br/>

Target Market(s)

B2B SMALL BUSINESS OWNERS
MARKETERS
ADVERTISERS

Industry/Entity Type

Digital Marketing

Number of Pages Required

3 page

Colors

Designer to choose colors to be used in the design.

Requirements
Must have
• MUST MATCH EXISTING THEME
Nice to have
• A VERY MODERN DESIGN

```html
<!DOCTYPE html>
<html lang="en">
<head>
<meta charset="utf-8">
<title>Sign Up – Brightloom Rewards</title>
<link href="https://fonts.googleapis.com/css2?family=Lato:wght@400;700&family=Raleway:wght@500;700;800&display=swap" rel="stylesheet">
<style>
:root{
  --dark:#1f1f1f;
  --blue:#0a72c9;
  --blue-card:#1e88d0;
  --grey-step:#909094;
  --text:#111;
  --row:#ededed;
  --card:#f8f8f8;
  --white:#fff;
  --foot-text:#d8d8d8;
}
*{box-sizing:border-box;margin:0;padding:0}
html,body{width:746px;height:1200px;overflow:hidden;background:var(--white)}
.page{position:relative;width:1440px;height:2316px;transform:scale(0.518);transform-origin:0 0;font-family:"Lato",sans-serif;color:var(--text)}
.abs{position:absolute}

/* header */
.top{left:0;top:0;width:1440px;height:110px;background:var(--dark)}
.brand{left:290px;top:38px;display:flex;align-items:center;gap:12px}
.brand-mark{width:30px;height:30px;background:var(--blue)}
.brand-name{font-family:"Raleway",sans-serif;font-weight:800;font-size:26px;color:#2a86d6;letter-spacing:1px}
.account{left:935px;top:0;display:flex;height:28px}
.account a{display:flex;align-items:center;gap:6px;padding:0 18px;font-size:12px;color:var(--white);text-decoration:none}
.account .login{background:#3b3b3b}
.account .signup{background:var(--blue)}
.phone-dot{left:876px;top:53px;width:35px;height:35px;border-radius:50%;background:var(--blue);display:flex;align-items:center;justify-content:center}
.phone-divider{left:926px;top:50px;width:1px;height:42px;background:#555}
.offices{left:942px;top:51px;color:var(--white);font-size:15px;line-height:22px}
.offices b{color:#fff}

.nav{left:0;top:110px;width:1440px;height:38px;background:var(--blue);display:flex;justify-content:center;align-items:center}
.nav a{color:var(--white);font-size:12px;text-decoration:none;padding:0 26px;border-right:1px solid rgba(255,255,255,.25);line-height:16px}
.nav a:first-child{padding-left:0}

.hero{left:0;top:148px;width:1440px;height:114px;background:linear-gradient(90deg,#a7a4cb 0%,#c0aacc 40%,#e2bbcc 70%,#f7c4a6 90%,#f9b892 100%);display:flex;align-items:center;justify-content:center}
.hero h1{font-family:"Lato",sans-serif;font-weight:400;font-size:26px;color:var(--white);letter-spacing:.5px}

/* steps */
.step-line{height:2px;top:391px}
.step{width:120px;text-align:center}
.step .dot{width:120px;height:120px;border-radius:50%;background:var(--grey-step);display:flex;align-items:center;justify-content:center}
.step.is-active .dot{background:var(--blue)}
.step .label{margin-top:18px;font-family:"Raleway",sans-serif;font-weight:700;font-size:17px;letter-spacing:.5px}

.intro{left:0;top:555px;width:1440px;text-align:center}
.intro h2{font-family:"Raleway",sans-serif;font-weight:800;font-size:29px;letter-spacing:.3px}
.intro p{margin:6px auto 0;width:800px;font-size:13.5px;line-height:24px}

/* cards */
.plan{background:var(--card);box-shadow:0 0 22px rgba(0,0,0,.12);padding:0 14px}
.plan-head{margin:0 -14px;background:var(--blue-card);color:var(--white);height:70px;padding:14px 16px 0}
.plan.is-featured .plan-head{background:var(--blue);padding-left:30px}
.plan-head h3{font-family:"Raleway",sans-serif;font-weight:800;font-size:24px;line-height:26px}
.plan-head p{font-size:11px;margin-top:2px}
.prices{list-style:none;margin-top:20px}
.prices li{position:relative;padding-left:33px;height:47px}
.radio{position:absolute;left:-1px;top:12px;width:20px;height:20px;border-radius:50%;background:#e2e2e2}
.radio.is-on::after{content:"";position:absolute;left:5px;top:5px;width:10px;height:10px;border-radius:50%;background:var(--blue)}
.prices strong{display:block;font-family:"Raleway",sans-serif;font-weight:800;font-size:17px;line-height:17px}
.prices span{display:block;font-size:11px;line-height:13px}
.features-title{font-family:"Raleway",sans-serif;font-weight:700;font-size:15px;margin:26px 0 11px 4px}
.features{list-style:none}
.features li{height:36px;padding:0 5px;display:flex;align-items:center;font-size:11px}
.features li:nth-child(odd){background:var(--row)}
.cta{display:flex;align-items:center;justify-content:center;height:47px;background:var(--blue);color:var(--white);font-family:"Raleway",sans-serif;font-weight:700;font-size:15px;text-decoration:none}

/* footer */
.footer{left:0;top:1806px;width:1440px;height:510px;background:var(--dark);color:var(--foot-text)}
.footer h4{font-weight:400;font-size:16px;color:var(--white);margin-bottom:10px}
.quick{left:289px;top:40px}
.quick ul{list-style:none}
.quick li{font-size:12px;line-height:24.3px}
.quick li::before{content:"›";margin-right:6px}
.contact{left:585px;top:40px;font-size:10.5px;line-height:15px}
.contact .row{display:flex;gap:8px;margin-bottom:40px}
.contact b{color:var(--white)}
.col-rule{top:40px;width:1px;height:180px;background:#2d2d2d}
.foot-brand{left:957px;top:44px;display:flex;align-items:center;gap:8px}
.foot-brand .brand-mark{width:18px;height:18px}
.foot-brand .brand-name{font-size:15px}
.socials{left:993px;top:76px;display:flex;gap:8px}
.socials span{width:26px;height:26px;border-radius:50%}
.copy{left:0;top:488px;width:1440px;text-align:center;font-size:12px;color:var(--white)}
</style>
</head>
<body>
<div class="page">

  <header class="top abs"></header>
  <div class="brand abs"><span class="brand-mark"></span><span class="brand-name">BRIGHTLOOM REWARDS</span></div>
  <div class="account abs">
    <a class="login" href="#">LOGIN</a>
    <a class="signup" href="#">SIGN UP</a>
  </div>
  <div class="phone-dot abs">
    <svg width="14" height="14" viewBox="0 0 24 24"><path fill="#fff" d="M6.6 10.8a15 15 0 0 0 6.6 6.6l2.2-2.2a1 1 0 0 1 1-.25 11.4 11.4 0 0 0 3.6.6 1 1 0 0 1 1 1V20a1 1 0 0 1-1 1A17 17 0 0 1 3 4a1 1 0 0 1 1-1h3.5a1 1 0 0 1 1 1c0 1.25.2 2.45.6 3.6a1 1 0 0 1-.25 1z"/></svg>
  </div>
  <div class="phone-divider abs"></div>
  <div class="offices abs">USA Office : <b>555-014-2290</b><br>International : <b>1-800-555-0147</b></div>

  <nav class="nav abs">
    <a href="#">HOME</a><a href="#">OUR INCENTIVES</a><a href="#">SAMPLES</a><a href="#">AFFILIATES</a><a href="#">TESTIMONIALS</a><a href="#">FAQ</a><a href="#">CONTACT</a>
  </nav>

  <section class="hero abs" role="img" aria-label="Soft sunset sky banner"><h1>SIGN UP</h1></section>

  <div class="step-line abs" style="left:479px;width:177px;background:#9a9a9a"></div>
  <div class="step-line abs" style="left:775px;width:178px;background:var(--blue)"></div>
  <div class="step abs" style="left:359px;top:331px">
    <div class="dot"><svg width="44" height="48" viewBox="0 0 44 48"><circle cx="22" cy="12" r="10" fill="#fff"/><path d="M2 48c0-14 8-22 20-22s20 8 20 22z" fill="#fff"/></svg></div>
    <div class="label">STEP 1</div>
  </div>
  <div class="step is-active abs" style="left:655px;top:331px">
    <div class="dot"><svg width="48" height="48" viewBox="0 0 48 48" fill="none" stroke="#fff" stroke-width="3" stroke-linejoin="round"><path d="M26 6h14v14L20 40 6 26z"/><circle cx="33" cy="13" r="2.5"/><path d="M18 30l8-8M19 23l1 1M24 29l1 1"/></svg></div>
    <div class="label">STEP 2</div>
  </div>
  <div class="step abs" style="left:952px;top:331px">
    <div class="dot"><svg width="48" height="38" viewBox="0 0 48 38" fill="none" stroke="#fff" stroke-width="3"><rect x="2" y="2" width="44" height="34" rx="4"/><path d="M2 12h44M2 18h44M24 27h14M24 32h8"/><circle cx="11" cy="28" r="3"/></svg></div>
    <div class="label">STEP 3</div>
  </div>

  <section class="intro abs">
    <h2>CHOOSE YOUR PROGRAM</h2>
    <p>Lorem ipsum dolor sit amet, consectetur adipiscing elit, sed do eiusmod tempor incididunt ut labore et dolore magna aliqua. Quis ipsum suspendisse ultrices gravida. Risus commodo viverra maecenas accumsan lacus vel facilisis.</p>
  </section>

  <!-- Trial -->
  <article class="plan abs" style="left:193px;top:721px;width:331px;height:955px">
    <div class="plan-head"><h3>TRIAL PROGRAM</h3><p>UNLIMITED AMOUNTS OF ALL THE CERTIFICATES</p></div>
    <ul class="prices" style="margin-top:21px">
      <li><i class="radio"></i><strong>$99/MTH</strong><span>MONTH TO MONTH BASIS NO CONTRACTS</span></li>
      <li><i class="radio is-on"></i><strong>$495</strong><span>ONE TIME PAYMENT FOR 6 MTHS OF SERVICE</span></li>
      <li><i class="radio"></i><strong>$2,295</strong><span>ONE TIME PAYMENT FOR 12 MONTHS OF SERVICE</span></li>
    </ul>
    <h4 class="features-title">FEATURES:</h4>
    <ul class="features">
      <li>UNLIMITED CERTIFICATE PDF DOWNLOADS</li><li>UNLIMITED E-MAIL CERTIFICATES</li><li>UNLIMITED TEXT/SMS CERTIFICATES</li><li>UNLIMITED API USAGE</li><li>UNLIMITED WEB BANNER CERTIFICATES</li><li>FULL REDEMPTION TRACKING</li><li>CERTIFICATE DISTRIBUTION REPORTS</li><li>WHITE LABEL REDEMPTION SITE</li><li>END USER MARKETING VIDEOS</li><li>MARKETING POSTERS AND FLYERS</li><li>PRODUCT DESCRIPTIONI BROCHURES</li><li>THE LATEST TIPS</li><li>SEPERATE REDEMPTION WEBSITES</li><li>CONTACT US 24/7</li><li>AFFILIATE PROGRAM</li><li>DISCOUNT TRAVEL BOOKING ENGINE</li>
    </ul>
    <a class="cta" href="#" style="margin-top:32px">CONTINUE</a>
  </article>

  <!-- Unlimited -->
  <article class="plan abs" style="left:901px;top:721px;width:332px;height:955px">
    <div class="plan-head"><h3>UNLIMITED PROGRAM</h3><p>UNLIMITED AMOUNTS OF ALL THE CERTIFICATE</p></div>
    <ul class="prices" style="margin-top:21px">
      <li><i class="radio"></i><strong>$99/MTH</strong><span>MONTH TO MONTH BASIS NO CONTRACTS</span></li>
      <li><i class="radio is-on"></i><strong>$495</strong><span>ONE TIME PAYMENT FOR 6 MTHS OF SERVICE</span></li>
      <li><i class="radio"></i><strong>$2,295</strong><span>ONE TIME PAYMENT FOR 12 MONTHS OF SERVICE</span></li>
    </ul>
    <h4 class="features-title">FEATURES:</h4>
    <ul class="features">
      <li>UNLIMITED CERTIFICATE PDF DOWNLOADS</li><li>UNLIMITED E-MAIL CERTIFICATES</li><li>UNLIMITED TEXT/SMS CERTIFICATES</li><li>UNLIMITED API USAGE</li><li>UNLIMITED WEB BANNER CERTIFICATES</li><li>FULL REDEMPTION TRACKING</li><li>CERTIFICATE DISTRIBUTION REPORTS</li><li>WHITE LABEL REDEMPTION SITE</li><li>END USER MARKETING VIDEOS</li><li>MARKETING POSTERS AND FLYERS</li><li>PRODUCT DESCRIPTIONI BROCHURES</li><li>THE LATEST TIPS</li><li>SEPERATE REDEMPTION WEBSITES</li><li>CONTACT US 24/7</li><li>AFFILIATE PROGRAM</li><li>DISCOUNT TRAVEL BOOKING ENGINE</li>
    </ul>
    <a class="cta" href="#" style="margin-top:32px">CONTINUE</a>
  </article>

  <!-- A la carte (featured) -->
  <article class="plan is-featured abs" style="left:525px;top:689px;width:375px;height:1016px;padding:0 15px;box-shadow:0 0 30px rgba(0,0,0,.18)">
    <div class="plan-head" style="margin:0 -15px"><h3>ALA CARTE PROGRAM</h3><p>1 CERTIFICATE TYPE EACH MONTH</p></div>
    <ul class="prices" style="margin-top:21px;padding-left:12px">
      <li><i class="radio"></i><strong>$49/MTH</strong><span>MONTH TO MONTH BASIS NO CONTRACTSE</span></li>
      <li><i class="radio"></i><strong>$239</strong><span>ONE TIME PAYMENT FOR 6 MTHS OF SERVICE</span></li>
      <li><i class="radio is-on"></i><strong>$399</strong><span>ONE TIME PAYMENT FOR 12 MONTHS OF SERVICE</span></li>
    </ul>
    <h4 class="features-title" style="margin-left:18px;margin-top:24px">FEATURES:</h4>
    <ul class="features">
      <li style="padding-left:18px">UNLIMITED CERTIFICATE PDF DOWNLOADS</li><li style="padding-left:18px">UNLIMITED E-MAIL CERTIFICATES</li><li style="padding-left:18px">UNLIMITED TEXT/SMS CERTIFICATES</li><li style="padding-left:18px">UNLIMITED API USAGE</li><li style="padding-left:18px">UNLIMITED WEB BANNER CERTIFICATES</li><li style="padding-left:18px">FULL REDEMPTION TRACKING</li><li style="padding-left:18px">CERTIFICATE DISTRIBUTION REPORTS</li><li style="padding-left:18px">WHITE LABEL REDEMPTION SITE</li><li style="padding-left:18px">END USER MARKETING VIDEOS</li><li style="padding-left:18px">MARKETING POSTERS AND FLYERS</li><li style="padding-left:18px">PRODUCT DESCRIPTIONI BROCHURES</li><li style="padding-left:18px">THE LATEST TIPS</li><li style="padding-left:18px">SEPERATE REDEMPTION WEBSITES</li><li style="padding-left:18px">CONTACT US 24/7</li><li style="padding-left:18px">AFFILIATE PROGRAM</li><li style="padding-left:18px">DISCOUNT TRAVEL BOOKING ENGINE</li>
    </ul>
    <a class="cta" href="#" style="margin-top:82px">CONTINUE</a>
  </article>

  <footer class="footer abs">
    <div class="quick abs">
      <h4>QUICK LINKS</h4>
      <ul>
        <li>Home</li><li>Our Incentives</li><li>Samples</li><li>Affiliate</li><li>Testimonials</li><li>Faq</li><li>Contact Us</li><li>Terms &amp; Conditions</li><li>Privacy Policy</li><li>Hoteliers</li><li>BLR PDF Flyer</li><li>BLR PDF Brochure</li><li>BLR Certificates List</li><li>How To Use BLR Certificates</li><li>Free Video Ad Mock Up For Marketing</li>
      </ul>
    </div>
    <div class="col-rule abs" style="left:574px"></div>
    <div class="contact abs">
      <h4>CONTACT DETAILS</h4>
      <div class="row">
        <svg width="11" height="14" viewBox="0 0 12 16"><path fill="#ccc" d="M6 0a6 6 0 0 0-6 6c0 4.5 6 10 6 10s6-5.5 6-10a6 6 0 0 0-6-6zm0 8.5A2.5 2.5 0 1 1 6 3.5a2.5 2.5 0 0 1 0 5z"/></svg>
        <div><b>Brightloom Rewards Group, Inc.</b><br>4410 Harbor View Lane<br>Coastview CA 90210</div>
      </div>
      <div class="row">
        <svg width="14" height="14" viewBox="0 0 14 14" fill="none" stroke="#ccc" stroke-width="1.2"><rect x="1" y="2" width="12" height="11"/><path d="M1 5h12M4 0v3M10 0v3M4 8h1M7 8h1M10 8h1M4 11h1M7 11h1"/></svg>
        <div>Hours: Mon-Fri 8am - 5pm PST<br>Sat-Sun CLOSED</div>
      </div>
    </div>
    <div class="col-rule abs" style="left:944px"></div>
    <div class="foot-brand abs"><span class="brand-mark"></span><span class="brand-name">BRIGHTLOOM REWARDS</span></div>
    <div class="socials abs">
      <span style="background:#3b5ba5"></span><span style="background:#e02a20"></span><span style="background:#0a72c9"></span><span style="background:#3d8ce8"></span>
    </div>
    <div class="copy abs">Copyright 2005-2020 Brightloom Rewards Group, Inc. All Rights Reserved.</div>
  </footer>

</div>
</body>
</html>
```